Vantro #27 - MEN'S NATURAL THERAPEUTIC INTIMATE WASH

Men's Natural Therapeutic INTIMATE Wash
VANTRO #27

Design a 4 oz. stand up tube with flip top cap...
To be packaged in a carton/box

Formula contains Tea Tree OIL
Aloe Vera Gel
Coconut Oil

PRODUCT IS A WASH/SOAP

Helps with
- Jock Itch (tinea cruris)
- Skin Rashes
- Candida
- Itchy Skin

COLORS ON TUBE: Gray, Black, Lime Electric Green and Blue

PRODUCT FOR MEN!

Target Market(s)

MEN

Industry/Entity Type

Retail

Font styles to use
Sans Serif

Colors
9bcb3b
abd036
33a6d7
000000
c9c9c9

Requirements
Must have
• Colors... black, gray, electric green and blue
Nice to have
• Needs to look masculine appeal to the male consumer

```html
<!DOCTYPE html>
<html lang="en">
<head>
<meta charset="utf-8">
<title>Vantro 27 – Men's Natural Therapeutic Intimate Wash</title>
<link rel="stylesheet" href="https://fonts.googleapis.com/css2?family=Questrial&family=Antonio:wght@300;400&family=Oswald:wght@500;600&display=swap">
<style>
  :root {
    --bg: #f4f8fb;
    --lime-top: #9bcb3b;
    --lime-mid: #c6e83a;
    --lime-bright: #d9f024;
    --lime-box: #abd036;
    --silver-light: #e6e6e6;
    --silver: #c9c9c9;
    --silver-dark: #a9a9a9;
    --cap: #1f1f1f;
    --cap-light: #3a3a3a;
    --ink: #000000;
    --white: #ffffff;
    --art-brown: #6b4a32;
    --art-green: #7fb24a;
  }
  * { margin: 0; padding: 0; box-sizing: border-box; }
  html, body { width: 1200px; height: 938px; overflow: hidden; background: var(--bg); }
  .canvas { position: relative; width: 1200px; height: 938px; }

  .tube { position: absolute; }
  .tube-body {
    position: absolute; left: 0; top: 0;
    background: linear-gradient(180deg, var(--lime-top) 0%, var(--lime-mid) 45%, var(--lime-bright) 75%, var(--lime-mid) 100%);
  }
  .tube-cap {
    position: absolute;
    background: linear-gradient(90deg, var(--cap) 0%, var(--cap-light) 50%, var(--cap) 100%);
    border-radius: 0 0 14px 14px;
  }
  .brand { position: absolute; color: var(--white); font-family: "Questrial", sans-serif; line-height: 1; }
  .brand-name, .brand-number { display: block; text-align: right; }
  .band {
    position: absolute; left: 0; right: 0;
    background: linear-gradient(180deg, var(--silver-dark) 0%, var(--silver-light) 30%, var(--silver) 70%, var(--silver-dark) 100%);
    color: var(--ink); text-align: center;
  }
  .band-sub { display: block; }
  .band-title { display: block; }
  .ingredients {
    position: absolute; background: var(--lime-box); border-radius: 4px;
    text-align: center; color: var(--ink); font-family: "Oswald", sans-serif;
  }
  .ingredients-label { display: block; color: var(--white); font-size: 4px; letter-spacing: 0.3px; }
  .ingredients-list { list-style: none; }
  .art { position: absolute; border-radius: 40%;
    background: radial-gradient(circle at 55% 55%, var(--art-brown) 0%, #a58a70 35%, var(--art-green) 60%, rgba(217,240,36,0) 75%); }
  .size { position: absolute; left: 0; right: 0; text-align: center; font-family: "Antonio", sans-serif; color: var(--ink); line-height: 1; }

  /* small tube */
  .tube--short { left: 324px; top: 268px; width: 286px; height: 536px; }
  .tube--short .tube-body { width: 286px; height: 440px; clip-path: polygon(0 0, 100% 0, 85% 100%, 15% 100%); }
  .tube--short .tube-cap { left: 42px; top: 440px; width: 202px; height: 96px; }
  .tube--short .brand { right: 62px; top: 46px; font-size: 35px; }
  .tube--short .band { top: 180px; height: 66px; padding-top: 8px; font-family: "Questrial", sans-serif; }
  .tube--short .band-sub { font-size: 15px; }
  .tube--short .band-title { font-size: 29px; letter-spacing: 0.5px; }
  .tube--short .ingredients { left: 94px; top: 250px; width: 99px; height: 52px; padding-top: 2px; font-size: 10px; line-height: 12px; }
  .tube--short .art { left: 48px; top: 304px; width: 156px; height: 108px; }
  .tube--short .size { top: 416px; font-size: 13px; }

  /* tall tube */
  .tube--tall { left: 650px; top: 96px; width: 238px; height: 736px; }
  .tube--tall .tube-body { width: 238px; height: 640px; clip-path: polygon(0 0, 100% 0, 91% 100%, 9% 100%); }
  .tube--tall .tube-cap { left: 43px; top: 640px; width: 152px; height: 96px; }
  .tube--tall .brand { right: 20px; top: 70px; font-size: 50px; }
  .tube--tall .band { top: 274px; height: 102px; padding-top: 12px; font-family: "Antonio", sans-serif; font-weight: 300; }
  .tube--tall .band-sub { font-size: 19px; }
  .tube--tall .band-title { font-size: 38px; line-height: 1.2; }
  .tube--tall .ingredients { left: 76px; top: 376px; width: 84px; height: 84px; padding-top: 4px; font-family: "Antonio", sans-serif; font-size: 13px; line-height: 18px; }
  .tube--tall .art { left: 42px; top: 468px; width: 152px; height: 128px; }
  .tube--tall .size { top: 604px; font-size: 15px; }
</style>
</head>
<body>
<main class="canvas">
  <section class="tube tube--short">
    <div class="tube-body">
      <div class="brand"><span class="brand-name">VANTRO</span><span class="brand-number">27</span></div>
      <div class="band"><span class="band-sub">Men's Natural Therapeutic</span><span class="band-title">INTIMATE WASH</span></div>
      <div class="ingredients">
        <span class="ingredients-label">FORMULA CONTAINS</span>
        <ul class="ingredients-list"><li>TEA TREE OIL</li><li>ALOE VERA GEL</li><li>COCONUT OIL</li></ul>
      </div>
      <div class="art" role="img" aria-label="Coconut halves, aloe vera slices and leaves with a water splash"></div>
      <div class="size">4 oz</div>
    </div>
    <div class="tube-cap"></div>
  </section>

  <section class="tube tube--tall">
    <div class="tube-body">
      <div class="brand"><span class="brand-name">VANTRO</span><span class="brand-number">27</span></div>
      <div class="band"><span class="band-sub">Men's Natural Therapeutic</span><span class="band-title">INTIMATE WASH</span></div>
      <div class="ingredients">
        <span class="ingredients-label">FORMULA CONTAINS</span>
        <ul class="ingredients-list"><li>TEA TREE OIL</li><li>ALOE VERA GEL</li><li>COCONUT OIL</li></ul>
      </div>
      <div class="art" role="img" aria-label="Coconut halves, aloe vera slices and leaves with a water splash"></div>
      <div class="size">4 oz</div>
    </div>
    <div class="tube-cap"></div>
  </section>
</main>
</body>
</html>
```